Pagevoより「最前線・空腹がすっと静まる献立&噛み方の手引き」というタイトルの電子書籍を出版予定です。

この本のコンセプトは「食べ物を選んで食べること&その食べ方で食欲が自然におさまること、更にはそれがダイエットと健康維持とアンチエイジングに非常に効果的であること、プラス今流行りのダイエット方(オートファジーダイエット、ミトコンドリア活性化、ケトジェニックダイエット、16時間断食、レクチンフリー 食品の勧め、腸活、SATエクササイズ、オイルの種類など)の説明とご提案(やり方)」をお伝えし、読者の皆様の健康維持に貢献したいということです。

ターゲットは男女ともに考えております。デザインは明るくて「何これ、ダイエットや食品の本にしては発想が新しい!」と興味を持ってもらえることを期待しております。(抽象的ですみません;)

何かご質問・ご提案がありましたらいつでもご連絡ください。
どうぞ宜しくお願いいたします。
*以下2項目の追加記載をお願いいたします。お手数ですがどうぞ宜しくお願いいたします。

・読者プレゼント
星座タイプ別 きみに向く減量術と献立チェック

・著者名: 森川 結奈
皆様、お忙しいところをたくさんのご応募、ありがとうございました!
どれも素敵なデザインでなかなか決めるのが難しいところではありますが、
数日中に決定、上位3名の方にご連絡いたします。

それでは、どうぞしばらくお待ちくださいませ。

取り急ぎ、お礼まで。

Thank you so much!
森川 結奈

当選:miru72_studio様 ー 明るくてフレッシュで清潔感のあるイメージで、何だろう?と書店だったら思わず手に取りたくなる素敵なデザインだと思いました。 次点:ripple_308様 ー デザインが可愛いく親しみやすいのと「食事を抑えるのでなく食欲を抑えるダイエット」など刺さるコピーがとても鋭いと感じました。執筆仲間にも好評でした。 次点: Hnbrook様 ー シンプルで見やすいが故に、逆に何が書いてあるんだろう?と興味を持たせてくれそうなデザインだと感じました。仲間内でも好評でした。

選定が遅くなり大変申し訳ございませんでした。この度は沢山の素敵なデザインをご提案くださり、ありがとうございました。 周りの者と相談の上、悩んだ末に決定させていただきました。 本当に素晴らしい作品ばかりで、デザインをするお仕事の素晴らしさを教えていただきました。 皆様のパワーにインスパイアされ、また二冊目も書きたいと思う原動力をいただきました。 またぜひご縁をいただけたら幸いです。 心より感謝申し上げます。どうもありがとうございました。 皆様のますますのご活躍とご発展をお祈り申し上げます。森川結奈

```html
<!DOCTYPE html>
<html lang="ja">
<head>
<meta charset="utf-8">
<title>最前線・空腹がすっと静まる献立&amp;噛み方の手引き</title>
<link rel="stylesheet" href="https://fonts.googleapis.com/css2?family=Zen+Maru+Gothic:wght@500;700;900&display=swap">
<style>
  :root {
    --sky: #a9dcf3;
    --sky-light: #e9f7fd;
    --blue: #2a7ec6;
    --red: #e2302a;
    --orange: #f47b20;
    --white: #ffffff;
    --skin: #f6d2b8;
    --dress: #bfe6f7;
    --veg-green: #7cbf4a;
  }
  * { margin: 0; padding: 0; box-sizing: border-box; }
  html, body { width: 720px; height: 1200px; overflow: hidden; }
  body { font-family: "Zen Maru Gothic", sans-serif; }
  .cover {
    position: relative; width: 720px; height: 1200px; overflow: hidden;
    background: radial-gradient(ellipse 70% 55% at 50% 48%, var(--white) 0%, var(--sky-light) 40%, var(--sky) 100%);
  }
  .figure-art {
    position: absolute; left: 190px; top: 90px; width: 340px; height: 680px;
    border-radius: 170px 170px 120px 120px;
    background: linear-gradient(180deg, #f1e3d6 0%, var(--skin) 30%, var(--dress) 62%, var(--veg-green) 78%, var(--dress) 100%);
    opacity: .85;
  }
  .badge {
    position: absolute; left: 283px; top: 20px; width: 154px; height: 154px;
    border-radius: 50%; background: var(--orange);
    color: var(--white); font-weight: 900; font-size: 40px;
    display: flex; align-items: center; justify-content: center; letter-spacing: 2px;
  }
  .vertical {
    position: absolute; writing-mode: vertical-rl; text-orientation: upright;
    color: var(--blue); font-weight: 700; line-height: 34px; white-space: nowrap;
    letter-spacing: 0;
  }
  .topics {
    left: 22px; top: 36px; height: 480px; font-size: 24px; text-align: end;
  }
  .concept { right: 24px; top: 44px; height: 330px; font-size: 24px; }
  .subtitle {
    position: absolute; left: 0; width: 720px; top: 512px; text-align: center;
    color: var(--red); font-weight: 900; font-size: 54px; letter-spacing: 2px;
    text-shadow: 0 0 4px var(--white), 0 0 4px var(--white), 0 0 6px var(--white);
  }
  .title-main {
    position: absolute; left: 0; width: 720px; top: 730px; text-align: center;
    color: var(--blue); font-weight: 900; font-size: 84px; letter-spacing: 2px;
  }
  .title-main .amp { font-size: 68px; margin: 0 10px; }
  .title-tail {
    position: absolute; left: 0; width: 720px; top: 868px; text-align: center;
    color: var(--blue); font-weight: 900; font-size: 70px; letter-spacing: 4px;
  }
  .author {
    position: absolute; left: 0; width: 720px; top: 1018px; text-align: center;
    color: var(--blue); font-weight: 700; font-size: 28px; letter-spacing: 3px;
  }
  .gift-band {
    position: absolute; left: 0; top: 1088px; width: 720px; height: 112px;
    background: var(--white);
  }
  .gift-label {
    position: absolute; left: -34px; top: 1044px; width: 230px; height: 60px;
    background: var(--orange); color: var(--white); border-radius: 30px;
    transform: rotate(-14deg); font-weight: 900; font-size: 26px; white-space: nowrap;
    display: flex; align-items: center; justify-content: center; padding-left: 34px;
  }
  .gift-text {
    position: absolute; left: 160px; top: 1098px; color: var(--blue);
    font-weight: 700; font-size: 33px; line-height: 1.45; letter-spacing: 1px;
  }
</style>
</head>
<body>
<main class="cover">
  <div class="figure-art" role="img" aria-label="野菜を抱えた女性のイラスト"></div>

  <div class="badge">最前線</div>

  <p class="vertical topics">オートファジーダイエット<br>ミトコンドリア活性化<br>ケトジェニックダイエット<br>一六時間断食<br>レクチンフリー食品の勧め　腸活<br>ＳＡＴエクササイズ　オイルの種類</p>

  <p class="vertical concept">食べ物を選んで食べる<br>その食べ方で食欲が自然におさまる<br>ダイエットと健康維持<br>アンチエイジングにも効果的</p>

  <h1>
    <span class="subtitle">空腹がすっと静まる</span>
    <span class="title-main">献立<span class="amp">&amp;</span>噛み方</span>
    <span class="title-tail">の手引き</span>
  </h1>

  <p class="author">森川 結奈 著</p>

  <div class="gift-band"></div>
  <div class="gift-label">読者プレゼント</div>
  <p class="gift-text">星座タイプ別<br>きみに向く減量術と献立チェック</p>
</main>
</body>
</html>
```